Mr Pellowes Yard Works flyer for newsletter

I need a professional looking flyer design for my company Mr Pellowes Yard Works based in New Braunfels, TX to boost sales. Must include the following: Lawn service starting at $40 (mowing, edging, leaf blowing) Tree trimming starting at $125. Other services-mulching, shrub trimming, aeration, flower bed maintenance, Fall/spring clean up. Serving New Braunfels and surrounding areas. To set up and estimate please call 512 555 0143 or email mrpellowesyard@example-mail.net

Industry/Entity Type

Landscaping

Font styles to use
Serif

Colors

Designer to choose colors to be used in the design.

Requirements
Must have
• Phone number 512 555 0143
• Email mrpellowesyard@example-mail.net

```html
<!DOCTYPE html>
<html lang="en">
<head>
<meta charset="utf-8">
<title>Mr Pellowes Yard Works Flyer</title>
<link rel="stylesheet" href="https://fonts.googleapis.com/css2?family=Bitter:wght@400;500;600&display=swap">
<style>
  :root {
    --page-bg: #e4e4e4;
    --paper: #ffffff;
    --brand-green: #3db54a;
    --accent-yellow: #f8f000;
    --ink: #3a3435;
    --rule: #c9c9c9;
    --separator: #e8552b;
    --photo-mower: #5fcf9a;
    --photo-grass: #3f9a35;
    --photo-grass-dark: #2f7f2a;
    --photo-tulip: #d0467a;
    --photo-tulip-sky: #e8eaea;
    --photo-leaves: #5a3b2c;
    --photo-leaves-light: #8a6a55;
  }
  * { box-sizing: border-box; margin: 0; padding: 0; }
  html, body { width: 1200px; height: 1200px; overflow: hidden; }
  body {
    background: var(--page-bg);
    font-family: "Bitter", Georgia, serif;
    color: var(--ink);
    position: relative;
  }
  .flyer {
    position: absolute;
    left: 175px;
    top: 0;
    width: 848px;
    height: 1200px;
    background: var(--paper);
  }
  .top-band {
    position: absolute; left: 0; top: 0; width: 100%; height: 12px;
    background: var(--accent-yellow);
  }
  .photo { position: absolute; }
  .photo--mower {
    left: 41px; top: 42px; width: 373px; height: 394px;
    background: linear-gradient(180deg, var(--photo-mower) 0%, #52c48a 30%, #3e8f3a 38%, var(--photo-grass) 55%, var(--photo-grass-dark) 100%);
  }
  .photo--tulips {
    left: 431px; top: 42px; width: 373px; height: 223px;
    background: linear-gradient(180deg, var(--photo-tulip-sky) 0%, #d9dcdc 28%, var(--photo-tulip) 40%, #c8567e 62%, #4f7a3c 100%);
  }
  .photo--leaves {
    left: 431px; top: 285px; width: 373px; height: 377px;
    background: radial-gradient(ellipse at 60% 62%, var(--photo-leaves-light) 0%, var(--photo-leaves) 55%, #4a3024 100%);
  }
  .brand-box {
    position: absolute; left: 41px; top: 458px; width: 373px; height: 204px;
    background: var(--brand-green);
    display: flex; align-items: center; justify-content: center;
  }
  .brand-name {
    color: #fff; font-weight: 500; font-size: 46px; line-height: 1.3;
    text-align: center;
  }
  .divider {
    position: absolute; left: 43px; top: 689px; width: 759px; height: 1px;
    background: var(--rule);
  }
  .column-rule {
    position: absolute; left: 424px; top: 707px; width: 1px; height: 205px;
    background: #6b6b6b;
  }
  .offer {
    position: absolute; top: 733px; width: 380px; text-align: center;
  }
  .offer--lawn { left: 43px; }
  .offer--trees { left: 427px; }
  .offer-title { font-size: 36px; font-weight: 500; line-height: 1.2; }
  .offer-lead { font-size: 27px; line-height: 1.4; }
  .offer-price {
    font-size: 62px; font-weight: 500; color: var(--brand-green);
    line-height: 1; margin-top: 20px; letter-spacing: -1px;
  }
  .service-list {
    position: absolute; left: 0; width: 100%; text-align: center;
    font-size: 23px; color: var(--brand-green);
  }
  .service-list--one { top: 944px; }
  .service-list--two { top: 986px; }
  .service-list .sep {
    display: inline-block; width: 2px; height: 28px;
    background: var(--separator); margin: 0 10px; vertical-align: -6px;
  }
  .contact-band {
    position: absolute; left: 0; top: 1066px; width: 100%; height: 134px;
    background: var(--accent-yellow); color: #111;
  }
  .contact-heading {
    position: absolute; top: 13px; width: 100%; text-align: center;
    font-size: 30px; font-weight: 500;
  }
  .contact-line {
    position: absolute; top: 66px; width: 100%; text-align: center;
    font-size: 23px; white-space: nowrap;
  }
  .contact-phone { font-size: 36px; font-weight: 500; margin-right: 20px; }
</style>
</head>
<body>
  <main class="flyer">
    <div class="top-band"></div>

    <div class="photo photo--mower" role="img" aria-label="Photo of a green lawn mower cutting lush grass"></div>
    <div class="photo photo--tulips" role="img" aria-label="Photo of a field of pink tulips with mountains behind"></div>
    <div class="photo photo--leaves" role="img" aria-label="Photo of an open hand holding dry brown leaves"></div>

    <div class="brand-box">
      <h1 class="brand-name">Mr. Pellowes<br>Yard Works</h1>
    </div>

    <div class="divider"></div>
    <div class="column-rule"></div>

    <section class="offer offer--lawn">
      <h2 class="offer-title">Lawn service</h2>
      <p class="offer-lead">starting at</p>
      <p class="offer-price">$40</p>
    </section>

    <section class="offer offer--trees">
      <h2 class="offer-title">Tree trimming</h2>
      <p class="offer-lead">starting at</p>
      <p class="offer-price">$125</p>
    </section>

    <p class="service-list service-list--one">mowing<span class="sep"></span>edging<span class="sep"></span>leaf blowing<span class="sep"></span>mulching<span class="sep"></span>shrub trimming</p>
    <p class="service-list service-list--two">aeration<span class="sep"></span>flower bed maintenance<span class="sep"></span>fall/spring&nbsp; clean up</p>

    <footer class="contact-band">
      <p class="contact-heading">To Set up and Estimate</p>
      <p class="contact-line">please call <span class="contact-phone">512 555 0143</span>email:mrpellowesyard@example-mail.net</p>
    </footer>
  </main>
</body>
</html>
```